Simple POSTER NEEDED by Snow Cone shop, Mobile food vendor

Snow Cone shop / Mobile food vendor needs artist to create a simple colorful graphic 24” x 18” poster for self-serve Snow Cone Flavor Station.
PLEASE SEE DOC "Snow Cone Poster Layout".
Children are the primary customer for our snow cones and the design should be made to appeal to them.
We are featuring 7 popular flavors on the poster. It will be mounted to a flat panel measuring 24” wide by 18” tall with spouts to dispense 7 different flavors.
The main body will be 1 coherent image with sunburst and logo at the top that ties everything together. The bottom 3” or more will be 7 columns of 7 different solid block of color clearly separated. And each with a different color representing that flavor and that spout and each column 2.75” wide.
The hole for each spout is 5/8” and the center of the hole will be 1.5” from the bottom. The spout will partly block the bottom 3.5” of the design.
The separation could be done by means of a solid block of color or by means of a snow cone up.
TEXT & LOGO Easily readable and creative text for each flavor will appear in each column to identify each flavor spout.
COLOR We want the design to look like we could be part of a 1,000 unit fast food franchise, polished and professional not tacky, yet appeal to our primary customer, kids. Perhaps we need to use muted colors or are they called soft or warm colors? Yet bold, bright, and vibrant colors. Please see document “SNOW CONE Poster Layout” to understand what we’re looking for. Please be creative and original. Some type of effect to the background color such as fading or color change might look good. The flavors and colors are: Blue Raspberry (blue) - Lemon Lime (green) - Wild Cherry (red) - Grape (purple) - Orange Pineapple (orange) - Piña Colada (white/slight pinkish/light yellow/creamy yellow) - Banana (yellow) (PLEASE don’t overlook the … ñ.) Rearrange the order of each color/flavor column as you see fit for best design.
IMPORTANT NOTE: The same logo and sunburst that you design for the top portion of the poster will need to be provided for us to print a 28" x 120" sign. PLEASE SEE DOC "Front Cart Signage". This is our logo "Pemvoxa" with a sunburst pattern behind.
We would like to see a variety of border effects around the logo. PLEASE BE CREATIVE AND GIVE US A VARIETY TO CONSIDER!
Thank you, and have fun!

```html
<!DOCTYPE html>
<html lang="en">
<head>
<meta charset="utf-8">
<title>Pemvoxa Snow Cone Flavor Station Poster</title>
<link href="https://fonts.googleapis.com/css2?family=Luckiest+Guy&family=Open+Sans:wght@400&display=swap" rel="stylesheet">
<style>
  :root {
    --stage: #001400;
    --rule: #ffffff;
    --sun-core: #fffbe6;
    --sun-mid: #ffd21a;
    --sun-edge: #f5941e;
    --brand-red: #ec1a0c;
    --pina: #f9a9dc;
    --pina-ink: #c8237f;
    --grape: #8c1fa6;
    --grape-ink: #4a0660;
    --blue: #1f4fb8;
    --blue-ink: #0a1f5e;
    --cherry: #d8140f;
    --cherry-ink: #7a0804;
    --orange: #ff9a0a;
    --orange-ink: #c24200;
    --banana: #ffea1a;
    --banana-ink: #7a6a00;
    --lime: #22b014;
    --lime-ink: #0a5204;
    --display: "Luckiest Guy", "Arial Rounded MT Bold", "Arial Black", "Helvetica Neue", sans-serif;
  }
  * { margin: 0; padding: 0; box-sizing: border-box; }
  html, body { width: 1200px; height: 1000px; overflow: hidden; background: var(--stage); }
  .canvas { position: relative; width: 1200px; height: 1000px; font-family: "Open Sans", sans-serif; }

  .dimension-width { position: absolute; left: 529px; top: 46px; width: 200px; text-align: center; color: var(--rule); font-size: 31px; }
  .dimension-width-rule { position: absolute; left: 93px; top: 96px; width: 1015px; height: 2px; background: var(--rule); }
  .dimension-height-rule { position: absolute; left: 68px; top: 122px; width: 2px; height: 758px; background: var(--rule); }
  .dimension-height { position: absolute; left: 44px; top: 510px; color: var(--rule); font-size: 31px; transform: translate(-50%, -50%) rotate(-90deg); white-space: nowrap; }

  .poster { position: absolute; left: 93px; top: 120px; width: 1015px; height: 760px; overflow: hidden; }
  .sunburst { position: absolute; inset: 0;
    background: radial-gradient(ellipse 70% 75% at 50% 55%, var(--sun-core) 0%, #ffe680 22%, var(--sun-mid) 50%, #fbb416 78%, var(--sun-edge) 100%); }

  .brand { position: absolute; left: 0; right: 0; top: 250px; text-align: center;
    font-family: var(--display); font-weight: 900; font-size: 124px; line-height: 1;
    color: var(--brand-red); letter-spacing: 1px; }

  .flavor-row { position: absolute; left: 200px; bottom: 0; width: 815px; height: 147px; display: flex; }
  .flavor { flex: 1; display: flex; align-items: center; justify-content: center; text-align: center;
    font-family: var(--display); font-weight: 900; font-size: 24px; line-height: 0.95; color: #fff;
    text-shadow:
      2px 0 0 var(--ink), -2px 0 0 var(--ink), 0 2px 0 var(--ink), 0 -2px 0 var(--ink),
      2px 2px 0 var(--ink), -2px 2px 0 var(--ink), 2px -2px 0 var(--ink), -2px -2px 0 var(--ink),
      3px 4px 0 var(--ink); }
  .flavor span { display: block; white-space: nowrap; }
  .flavor-pina   { --ink: var(--pina-ink);   background: radial-gradient(circle at 50% 55%, #ffe0f3, var(--pina) 70%); color: #fff9c2; font-size: 26px; }
  .flavor-grape  { --ink: var(--grape-ink);  background: radial-gradient(circle at 50% 55%, #c24ee0, var(--grape) 75%); font-size: 28px; }
  .flavor-blue   { --ink: var(--blue-ink);   background: radial-gradient(circle at 50% 55%, #3f7be6, var(--blue) 75%); font-size: 19px; }
  .flavor-cherry { --ink: var(--cherry-ink); background: radial-gradient(circle at 50% 55%, #f2443a, var(--cherry) 75%); font-size: 28px; }
  .flavor-orange { --ink: var(--orange-ink); background: radial-gradient(circle at 50% 55%, #ffc24a, var(--orange) 75%); font-size: 18px; }
  .flavor-banana { --ink: var(--banana-ink); background: radial-gradient(circle at 50% 55%, #fff680, var(--banana) 75%); color: #fffbe0; font-size: 22px; }
  .flavor-lime   { --ink: var(--lime-ink);   background: radial-gradient(circle at 50% 55%, #5fd94a, var(--lime) 75%); font-size: 27px; }
</style>
</head>
<body>
<div class="canvas">
  <div class="dimension-width">24 inch</div>
  <div class="dimension-width-rule"></div>
  <div class="dimension-height-rule"></div>
  <div class="dimension-height">18 inch</div>

  <section class="poster">
    <div class="sunburst" role="img" aria-label="Golden sunburst background with rays radiating from a bright centre"></div>
    <h1 class="brand">Pemvoxa</h1>

    <div class="flavor-row">
      <div class="flavor flavor-pina"><div><span>Piña</span><span>Colada</span></div></div>
      <div class="flavor flavor-grape"><div><span>Grape</span></div></div>
      <div class="flavor flavor-blue"><div><span>Blue</span><span>Raspberry</span></div></div>
      <div class="flavor flavor-cherry"><div><span>Wild</span><span>Cherry</span></div></div>
      <div class="flavor flavor-orange"><div><span>Orange</span><span>Pineapple</span></div></div>
      <div class="flavor flavor-banana"><div><span>Banana</span></div></div>
      <div class="flavor flavor-lime"><div><span>Lemon</span><span>Lime</span></div></div>
    </div>
  </section>
</div>
</body>
</html>
```